Redesign existing website

We would like a redesign of the website http://www.velbrisanalytics.com that creates a more modern, up to date look.

Velbris Analytics creates software for social science research and is focused on making the software user friendly and easy to use. We would like to convey seriousness, but also
a very up to date, just released look.

Feel free to modify the logo if you wish.

Target Market(s)

Academics, researchers

Industry/Entity Type

Software

Requirements
Must have
• The design should incorporate the same information as the current website.

```html
<!DOCTYPE html>
<html lang="en">
<head>
<meta charset="utf-8">
<title>Velbris Analytics — About Us</title>
<link href="https://fonts.googleapis.com/css2?family=Arimo:ital,wght@0,400;0,700;1,700&family=Poiret+One&display=swap" rel="stylesheet">
<style>
:root{
  --light:#c0c0c0;
  --light-edge:#d2d2d2;
  --black:#0c0c0c;
  --mid:#6b6b6b;
  --map:#262626;
  --navy:#1c2a4f;
  --ink:#111;
  --white:#fff;
  --muted:#555;
}
*{margin:0;padding:0;box-sizing:border-box}
html,body{width:996px;height:1200px;overflow:hidden}
body{position:relative;background:var(--black);font-family:"Arimo",Arial,sans-serif;color:var(--ink)}
.abs{position:absolute}
.band{position:absolute;left:0;width:996px}
.band-top{top:0;height:44px;background:var(--light)}
.hero{top:44px;height:323px;background:var(--black)}
.light{background:var(--light);border-top:4px solid var(--light-edge)}
.mid{background:var(--mid);border-top:3px solid #7a7a7a}
.world-map{left:195px;top:62px;width:612px;height:278px;background:radial-gradient(ellipse at center,#2c2c2c 0%,#1a1a1a 70%,var(--black) 100%);border-radius:40px}
.nav{position:absolute;display:flex;justify-content:space-around;align-items:center;background:var(--light);font-size:11px;color:var(--ink)}
.nav a{color:inherit;text-decoration:none}
.nav-top{left:465px;top:44px;width:354px;height:30px;border-top:3px solid #888}
.nav-foot{left:321px;top:1163px;width:352px;height:37px}
.brand{left:214px;top:12px;width:200px;text-align:center}
.brand-mark{display:block;margin:0 auto 6px;width:78px;height:78px;border-radius:50%;background:var(--navy);border:4px solid #ddd}
.brand-name{font-size:17px;font-weight:700;color:var(--white);letter-spacing:.5px}
.tagline{right:190px;top:172px;text-align:right;font-family:"Poiret One",sans-serif;font-size:20px;line-height:18px;color:var(--white)}
.tab{position:absolute;height:37px;display:flex;align-items:center;justify-content:center;font-size:13px;font-weight:700;color:var(--white);background:linear-gradient(90deg,#eee 0%,#333 25%,#444 75%,#eee 100%);box-shadow:0 14px 12px -8px rgba(0,0,0,.55)}
.notch{position:absolute;width:78px;height:39px;border-radius:39px 39px 0 0;background:var(--light)}
.copy{position:absolute;font-size:11px;line-height:18px}
.copy-dark{color:var(--ink)}
.copy-light{color:var(--white)}
.read-more{position:absolute;width:116px;height:31px;background:var(--white);border-radius:8px 8px 0 0;display:flex;align-items:center;padding-left:17px;gap:6px;font-size:11px;color:var(--muted)}
.person{position:absolute;left:193px}
.person-name{font-size:23px;font-weight:700;color:var(--navy);line-height:24px}
.person-role{font-size:18px;font-weight:700;font-style:italic;line-height:22px}
.role-dark{color:#3a3a3a}
.role-white{color:var(--white)}
</style>
</head>
<body>
<div class="band band-top"></div>
<div class="band hero"></div>
<div class="abs world-map" role="img" aria-label="Dotted world map in dark grey across the header"></div>

<header>
  <div class="abs brand"><span class="brand-mark"></span><span class="brand-name">Velbris Analytics</span></div>
  <nav class="nav nav-top"><a>Home</a><a>Products</a><a>News</a><a>About Us</a><a>Contact Us</a></nav>
  <p class="abs tagline">Increasing the power and<br>efficiency of empirical<br>social science research</p>
</header>

<div class="notch" style="left:734px;top:334px"></div>
<section class="band light" style="top:367px;height:176px"></section>
<div class="tab" style="left:255px;top:339px;width:125px">About Us</div>
<p class="copy copy-dark" style="left:233px;top:436px;width:562px">The mission of Velbris Analytics, Inc. is to produce software products that multiply the power and efficiency of empirical research in the social sciences. A central goal is to expand access to complex data sources and to the advanced methods of scientific investigation needed to analyze them. The company was established in January 2005 by the Halvorsen family.</p>

<section class="band mid" style="top:559px;height:169px"></section>
<div class="tab" style="left:255px;top:575px;width:215px">The Halvorsen Family</div>
<p class="copy copy-light" style="left:232px;top:646px;width:580px">The members of the Halvorsen family have a long tradition of accomplishment in the development of statistical measures and in data management and dissemination.</p>

<svg width="0" height="0" style="position:absolute"><defs><g id="chev"><path d="M1 3l11 11L23 3M5 1l7 8 7-8" fill="none" stroke="#555" stroke-width="1.2"/></g></defs></svg>

<div class="read-more" style="left:732px;top:697px">Read More<svg width="24" height="16"><use href="#chev"/></svg></div>

<div class="notch" style="left:227px;top:739px"></div>
<section class="band light" style="top:771px;height:125px"></section>
<div class="person" style="top:821px"><p class="person-name">Daniel Halvorsen,</p><p class="person-role role-dark">President and CEO</p></div>
<div class="read-more" style="left:732px;top:865px">Read More<svg width="24" height="16"><use href="#chev"/></svg></div>

<div class="person" style="top:933px"><p class="person-name">Marion Halvorsen</p><p class="person-role role-white">Vice President for Product Development and CTO</p></div>
<div class="read-more" style="left:732px;top:988px">Read More<svg width="24" height="16"><use href="#chev"/></svg></div>

<section class="band light" style="top:1019px;height:130px"></section>
<div class="person" style="top:1057px"><p class="person-name">Elise Halvorsen</p><p class="person-role role-white">Vice President for Research</p></div>
<div class="read-more" style="left:732px;top:1118px">Read More<svg width="24" height="16"><use href="#chev"/></svg></div>

<footer>
  <nav class="nav nav-foot"><a>Home</a><a>Products</a><a>News</a><a>About Us</a><a>Contact Us</a></nav>
</footer>
</body>
</html>
```